School Website

I need a design for a School (2 sections: Primary 6-12 years and Secondary 12-18 years). The first page is just a choice of the 2 sections. After we'll need 2 websites (with the same structure: Menu, ...) but with different colors. In fact, we need for end of October, 6 design of school website. So the best websites are going to be made available to you in the future (in pixmarketo) but privately.

Target Market(s)

Public, Parents, ...

Coding

Coded - Design and coding required

Number of Pages Required

5+ page

Font styles to use
Sans Serif

Colors
34a6d7
85cae6
cee9f5
ffffff

Requirements
Must have
• You can check the old Website: http: / /velmoq.be We need the same pages with the same content. Menu: - HomePage - News and communication (like blog page) - Activities (like blog page, with photo gallery) - Contact (Contact form + maps) - In the main menu, we need a special button to connect to an external Website ( button needs to be different than the other menu items The name of this button is "Parents Area"). The logo of 2 sections are attached. Please use it for the design and the choice of colors.
Nice to have
• This is a web design of other school that we like: https://www.quintel.be

```html
<!DOCTYPE html>
<html lang="en">
<head>
<meta charset="utf-8">
<title>Royal Athenaeum of Velmont</title>
<link href="https://fonts.googleapis.com/css2?family=Lato:wght@300;400;700;900&display=swap" rel="stylesheet">
<style>
:root{
  --blue:#34a6d7;
  --blue-mid:#85cae6;
  --blue-light:#cee9f5;
  --white:#ffffff;
  --green:#8cc63e;
  --ink:#2b2b2b;
  --text:#5e5e5e;
  --grey-band:#f1f1f1;
  --footer:#262626;
  --footer-deep:#1b1b1b;
}
*{box-sizing:border-box;margin:0;padding:0}
html,body{width:1200px;height:4504px;overflow:hidden}
body{font-family:"Lato",Arial,sans-serif;color:var(--text);background:var(--white);position:relative;font-size:13px}
.abs{position:absolute}
.h2{font-size:34px;font-weight:700;color:var(--ink);text-align:center}
.rule{width:60px;height:3px;background:var(--blue);margin:10px auto 0}

/* top bar */
.topbar{left:0;top:0;width:1200px;height:32px;background:var(--blue);color:var(--white);font-size:11px}
.topbar .info{left:172px;top:9px;display:flex;gap:26px;align-items:center}
.topbar .info span{display:flex;align-items:center;gap:6px}
.topbar .social{left:850px;top:9px;display:flex;gap:10px}
.topbar .social i{width:14px;height:14px;border-radius:50%;background:rgba(255,255,255,.85);display:block}
.parents-btn{left:930px;top:0;width:100px;height:32px;background:var(--green);color:var(--white);font-size:11px;font-weight:700;display:flex;align-items:center;justify-content:center;text-transform:uppercase}

/* nav */
.nav{left:0;top:32px;width:1200px;height:80px;background:var(--white);box-shadow:0 2px 6px rgba(0,0,0,.06)}
.brand{left:172px;top:22px;display:flex;align-items:center;gap:10px}
.brand i{width:34px;height:34px;border-radius:50%;background:var(--blue);display:block}
.brand b{font-size:17px;font-weight:700;color:var(--blue)}
.menu{left:660px;top:32px;display:flex;gap:26px;font-size:14px;color:var(--ink)}
.menu .active{color:var(--blue);border-bottom:2px solid var(--blue);padding-bottom:4px}

/* hero */
.hero{left:0;top:112px;width:1200px;height:448px;background:linear-gradient(100deg,#4d5a63 0%,#7c8a92 35%,#c9cfd1 60%,#e6d8c4 80%,#b49a7c 100%)}
.hero .shade{left:0;top:0;width:620px;height:448px;background:linear-gradient(90deg,rgba(20,30,40,.45),rgba(20,30,40,0))}
.hero h1{left:172px;top:150px;font-size:44px;line-height:52px;font-weight:700;color:var(--white)}
.hero p{left:172px;top:262px;font-size:17px;color:#d6f0a8}
.quicklinks{left:160px;top:536px;width:860px;height:70px;background:var(--blue);display:flex;color:var(--white);font-size:11px;font-weight:700;text-transform:uppercase;box-shadow:0 6px 16px rgba(0,0,0,.15)}
.quicklinks a{flex:1;display:flex;align-items:center;justify-content:center;border-right:1px solid rgba(255,255,255,.35)}
.quicklinks a:last-child{border-right:none}

/* schedules */
.schedules h2{left:172px;top:722px;font-size:34px;font-weight:700;color:var(--ink)}
.schedules .lead{left:172px;top:786px;font-size:14px;font-weight:700;color:var(--ink)}
.schedules ul{left:172px;top:818px;width:470px;list-style:none;font-size:13px;line-height:19px}
.schedules li{display:flex;gap:10px;margin-bottom:10px}
.schedules li svg{flex:none;margin-top:3px}
.schedules .note{left:200px;top:1116px;width:440px;font-size:13px;font-weight:700;color:var(--ink);line-height:19px}
.schedules .photo{left:680px;top:688px;width:240px;height:512px;background:linear-gradient(160deg,#d8e3b0,#7fb0c9 45%,#d2875a 80%,#e8e0c8)}

/* useful info */
.useful .h2{left:0;top:1300px;width:1200px}
.info-col{top:1400px;width:240px;text-align:center;font-size:12px;line-height:17px}
.info-col .icon{width:64px;height:64px;border-radius:50%;background:var(--green);margin:0 auto 14px;display:flex;align-items:center;justify-content:center}
.info-col h3{font-size:13px;font-weight:700;color:var(--ink);margin-bottom:6px}
.info-col a{display:block;color:var(--blue);margin-top:8px}

/* meals */
.meals{left:0;top:1680px;width:1200px;height:420px;background:var(--grey-band)}
.meals .photo{left:172px;top:0;width:488px;height:420px;background:linear-gradient(135deg,#c9c1a4,#8aa37a 45%,#6b7f6c 70%,#c7b890)}
.meals h2{left:700px;top:116px;width:330px;text-align:center;font-size:38px;font-weight:700;color:var(--ink)}
.meals p{left:720px;top:186px;width:290px;text-align:center;font-size:13px;line-height:19px}
.btn-green{background:var(--green);color:var(--white);font-size:12px;font-weight:700;display:flex;align-items:center;justify-content:center;border-radius:3px}
.meals .btn-green{left:810px;top:300px;width:110px;height:36px}

/* news */
.news .h2{left:0;top:2166px;width:1200px}
.news .sub{left:0;top:2212px;width:1200px;text-align:center;font-size:13px}
.card{width:264px;background:var(--white);box-shadow:0 2px 10px rgba(0,0,0,.1)}
.card .img{height:130px}
.card .body{padding:12px 14px}
.card h3{font-size:13px;font-weight:700;color:var(--ink);line-height:17px;margin-bottom:6px}
.card p{font-size:11px;line-height:15px}
.card .meta{display:flex;gap:16px;margin-top:12px;padding-top:8px;border-top:1px solid #eee;font-size:10px;color:var(--blue)}
.dots{display:flex;gap:6px;justify-content:center}
.dots i{width:8px;height:8px;border-radius:50%;background:#c8c8c8;display:block}
.dots i.on{background:var(--blue)}

/* team */
.team{left:0;top:2600px;width:1200px;height:648px;background:linear-gradient(180deg,#3d5f74,#557b91 50%,#6f8fa1)}
.team .h2{left:0;top:60px;width:1200px;color:var(--white)}
.tabs{left:0;top:118px;width:1200px;display:flex;justify-content:center;gap:4px;font-size:12px}
.tabs span{padding:8px 18px;background:var(--blue);color:var(--white)}
.tabs span.on{background:var(--green)}
.member{top:200px;width:264px;height:210px;background:var(--white);text-align:center;padding-top:70px}
.member .avatar{position:absolute;left:92px;top:-40px;width:80px;height:80px;border-radius:50%;background:linear-gradient(160deg,#d9b99b,#8a6a55);border:4px solid var(--white)}
.member h3{font-size:15px;color:var(--blue);font-weight:700}
.member p{font-size:12px;margin-top:6px}
.member .soc{display:flex;gap:6px;justify-content:center;margin-top:16px}
.member .soc i{width:22px;height:22px;border-radius:50%;border:1px solid #bbb;display:block}

/* activities */
.activities .h2{left:0;top:3310px;width:1200px}
.filters{left:0;top:3394px;width:1200px;display:flex;justify-content:center;gap:8px;font-size:11px}
.filters span{padding:6px 16px;border:1px solid #ddd;color:var(--text)}
.filters span.on{background:var(--blue);border-color:var(--blue);color:var(--white)}
.act{width:264px;background:var(--white);box-shadow:0 2px 10px rgba(0,0,0,.1)}
.act p{padding:12px 14px 6px;font-size:12px;color:var(--ink)}
.act .bar{margin:0 14px 14px;width:60px;height:3px;background:var(--blue)}

/* footer */
.footer{left:0;top:4120px;width:1200px;height:340px;background:var(--footer)}
.footer .intro{left:172px;top:56px;width:400px;font-size:12px;line-height:18px;color:#ddd}
.field{background:#3a3a3a;color:#aaa;font-size:11px;padding:9px 12px}
.f1{left:172px;top:112px;width:196px;height:34px}
.f2{left:376px;top:112px;width:196px;height:34px}
.f3{left:172px;top:154px;width:400px;height:90px}
.footer .btn-green{left:172px;top:254px;width:400px;height:34px;border-radius:0}
.contact-card{left:612px;top:30px;width:416px;height:280px;background:var(--white)}
.contact-card .txt{padding:16px 18px;font-size:12px;line-height:18px;color:var(--ink)}
.contact-card .map{position:absolute;left:0;top:76px;width:416px;height:204px;background:linear-gradient(135deg,#e9ecef,#d7e2d0 50%,#cfdde8)}
.copy{left:0;top:4460px;width:1200px;height:44px;background:var(--footer-deep);color:#aaa;font-size:11px;display:flex;align-items:center;justify-content:center}
</style>
</head>
<body>

<div class="abs topbar">
  <div class="abs info">
    <span><svg width="10" height="12" viewBox="0 0 10 12"><path d="M5 0a4 4 0 0 0-4 4c0 3 4 8 4 8s4-5 4-8a4 4 0 0 0-4-4zm0 5.5A1.5 1.5 0 1 1 5 2.5a1.5 1.5 0 0 1 0 3z" fill="#fff"/></svg>Rue des Tilleuls 12, 4580 Velmont, Belgium</span>
    <span><svg width="11" height="11" viewBox="0 0 12 12"><path d="M2.5 0l2 3-1.3 1.3a7 7 0 0 0 4.5 4.5L9 7.5l3 2-1.5 2.5C5 12 0 7 0 1.5z" fill="#fff"/></svg>+32 81 40 55 17</span>
  </div>
  <div class="abs social"><i></i><i></i><i></i><i></i></div>
  <div class="abs parents-btn">Parents Area</div>
</div>

<header class="abs nav">
  <div class="abs brand"><i></i><b>Athénée Royal de Velmont</b></div>
  <nav class="abs menu"><span class="active">Home</span><span>News and communication</span><span>Activities</span><span>Contact</span></nav>
</header>

<section class="abs hero" role="img" aria-label="Photo of two smiling school children in a classroom">
  <div class="abs shade"></div>
  <h1 class="abs">Royal Athenaeum<br>of Velmont</h1>
  <p class="abs">Kindergarten and Primary</p>
</section>
<div class="abs quicklinks"><a>Break from 28 to 1 November 2019</a><a>Rules of procedure</a><a>New activities</a></div>

<section class="schedules">
  <h2 class="abs">Our schedules and daycare</h2>
  <div class="abs lead">Class schedules are defined as follows:</div>
  <ul class="abs">
    <li><svg width="12" height="10" viewBox="0 0 12 10"><path d="M1 5l3.5 3.5L11 1" stroke="#34a6d7" stroke-width="2" fill="none"/></svg>Every day from 8.25 am to 3.25 pm (except on Wednesdays from 8.25 am to 12.20 pm).</li>
    <li><svg width="12" height="10" viewBox="0 0 12 10"><path d="M1 5l3.5 3.5L11 1" stroke="#34a6d7" stroke-width="2" fill="none"/></svg>A daycare is organized from 7.00 am in the buildings of the primary section.</li>
    <li><svg width="12" height="10" viewBox="0 0 12 10"><path d="M1 5l3.5 3.5L11 1" stroke="#34a6d7" stroke-width="2" fill="none"/></svg>At the end of the lessons, the children are supervised by the holders and then taken care of in nursery from 15:30 and at the latest until 18:00.</li>
    <li><svg width="12" height="10" viewBox="0 0 12 10"><path d="M1 5l3.5 3.5L11 1" stroke="#34a6d7" stroke-width="2" fill="none"/></svg>On Wednesdays from 12:30 to 18:00, different activities are offered depending on the weather.</li>
    <li><svg width="12" height="10" viewBox="0 0 12 10"><path d="M1 5l3.5 3.5L11 1" stroke="#34a6d7" stroke-width="2" fill="none"/></svg>The morning and Wednesday nurseries are paid. Decreasing price according to the number of children per family.</li>
  </ul>
  <div class="abs note">Only those children whose parents have provided a certificate from their employer specifying the hours of work will be accepted at the day care centre.</div>
  <div class="abs photo" role="img" aria-label="Photo of a child stacking colourful toy blocks"></div>
</section>

<section class="useful">
  <div class="abs h2">Useful Information<div class="rule"></div></div>
  <div class="abs info-col" style="left:196px">
    <div class="icon"><svg width="28" height="28" viewBox="0 0 28 28"><rect x="6" y="4" width="16" height="20" rx="2" stroke="#fff" stroke-width="2" fill="none"/><path d="M10 10h8M10 14h8M10 18h5" stroke="#fff" stroke-width="2"/></svg></div>
    <h3>Rules of procedure</h3><p>Please find attached the rules of procedure</p><a>View more</a>
  </div>
  <div class="abs info-col" style="left:480px">
    <div class="icon"><svg width="28" height="28" viewBox="0 0 28 28"><path d="M3 11l11-6 11 6-11 6z" stroke="#fff" stroke-width="2" fill="none"/><path d="M8 14v6c3 3 9 3 12 0v-6" stroke="#fff" stroke-width="2" fill="none"/></svg></div>
    <h3>Educational and educational project</h3><p>Please find attached the educational and educational project of the school network</p><a>View more</a>
  </div>
  <div class="abs info-col" style="left:764px">
    <div class="icon"><svg width="28" height="28" viewBox="0 0 28 28"><rect x="4" y="6" width="20" height="18" rx="2" stroke="#fff" stroke-width="2" fill="none"/><path d="M4 11h20M9 3v5M19 3v5" stroke="#fff" stroke-width="2"/></svg></div>
    <h3>School holidays</h3><p>2019-2020 school year</p><a>View more</a>
  </div>
</section>

<section class="abs meals">
  <div class="abs photo" role="img" aria-label="Photo of a bright school canteen with tables and chairs"></div>
  <h2 class="abs">Meals Offered</h2>
  <p class="abs">To the children of the nursery section of the Royal Athenaeum during the whole school year! Meal project for your little ones, our little ones, of the Velmont Kitchen. What's more!</p>
  <div class="abs btn-green">View More</div>
</section>

<section class="news">
  <div class="abs h2">Latest News and communication</div>
  <div class="abs sub">Education &amp; Communication news</div>
  <article class="abs card" style="left:168px;top:2272px">
    <div class="img" role="img" aria-label="Photo of children on stage at a school event" style="background:linear-gradient(135deg,#2f6e4d,#c54a3a 55%,#e0b14a)"></div>
    <div class="body"><h3>Royal Athenaeum of Velmont school organized the communication...</h3><p>Sed ut perspiciatis unde omnis iste natus error sit voluptatem accusantium doloremque.</p><div class="meta"><span>28/09/2019</span><span>12</span></div></div>
  </article>
  <article class="abs card" style="left:468px;top:2272px">
    <div class="img" role="img" aria-label="Photo of a plant on a desk" style="background:linear-gradient(135deg,#f1ede4,#a9c48b 55%,#d9d2c2)"></div>
    <div class="body"><h3>eNeducation – Latest September 2019 – The Big One</h3><p>Sed ut perspiciatis unde omnis iste natus error sit voluptatem accusantium doloremque.</p><div class="meta"><span>26/09/2019</span><span>8</span></div></div>
  </article>
  <article class="abs card" style="left:768px;top:2272px">
    <div class="img" role="img" aria-label="Photo of the new indoor playground" style="background:linear-gradient(135deg,#c58a52,#e7c99a 50%,#8a5a36)"></div>
    <div class="body"><h3>New indoor playground</h3><p>Sed ut perspiciatis unde omnis iste natus error sit voluptatem accusantium doloremque.</p><div class="meta"><span>20/09/2019</span><span>5</span></div></div>
  </article>
  <div class="abs dots" style="left:0;top:2530px;width:1200px"><i class="on"></i><i></i><i></i></div>
</section>

<section class="abs team" role="img" aria-label="Blue-tinted background photo of a school crowd">
  <div class="abs h2">Meet Our Team</div>
  <div class="abs tabs"><span class="on">Kindergarten section</span><span>Primary section</span><span>Educators</span></div>
  <div class="abs member" style="left:168px"><div class="avatar" role="img" aria-label="Portrait photo of a teacher"></div><h3>Sandrine MOREL</h3><p>Holder of the class of M3</p><div class="soc"><i></i><i></i><i></i><i></i></div></div>
  <div class="abs member" style="left:468px"><div class="avatar" role="img" aria-label="Portrait photo of a teacher"></div><h3>Mrs Claire DUVAL</h3><p>Holder of the class of M1-M2</p><div class="soc"><i></i><i></i><i></i><i></i></div></div>
  <div class="abs member" style="left:768px"><div class="avatar" role="img" aria-label="Portrait photo of a teacher"></div><h3>Mrs Lucia BERNARDI</h3><p>Holder of the class of M3</p><div class="soc"><i></i><i></i><i></i><i></i></div></div>
  <div class="abs dots" style="left:0;top:434px;width:1200px"><i class="on"></i><i></i><i></i></div>
</section>

<section class="activities">
  <div class="abs h2">Our Activities</div>
  <div class="abs filters"><span class="on">All</span><span>Summer</span><span>After Schools</span><span>STEM education</span><span>Indoor Games</span></div>
  <div class="abs act" style="left:168px;top:3456px"><div role="img" aria-label="Photo of children painting" style="height:160px;background:linear-gradient(135deg,#e8c9a3,#6fa6c7 60%,#f0e2c8)"></div><p>Sed ut perspiciatis unde omnis</p><div class="bar"></div></div>
  <div class="abs act" style="left:468px;top:3456px"><div role="img" aria-label="Photo of children working in class" style="height:160px;background:linear-gradient(135deg,#d6b58e,#9cc0d4 55%,#e6d3b8)"></div><p>Sed ut perspiciatis unde omnis</p><div class="bar"></div></div>
  <div class="abs act" style="left:768px;top:3456px"><div role="img" aria-label="Photo of children playing indoors" style="height:160px;background:linear-gradient(135deg,#cfd6da,#a5b6a0 55%,#ece5da)"></div><p>Sed ut perspiciatis unde omnis</p><div class="bar"></div></div>
  <div class="abs act" style="left:168px;top:3708px"><div role="img" aria-label="Photo of an amusement park ride" style="height:210px;background:linear-gradient(135deg,#6aa6d6,#d44a3e 50%,#f0c04a)"></div><p>Sed ut perspiciatis unde omnis</p><div class="bar"></div></div>
  <div class="abs act" style="left:468px;top:3708px"><div role="img" aria-label="Photo of children drawing at a table" style="height:210px;background:linear-gradient(135deg,#f2d4a8,#8fc1d9 55%,#e8b96c)"></div><p>Sed ut perspiciatis unde omnis</p><div class="bar"></div></div>
  <div class="abs act" style="left:768px;top:3708px"><div role="img" aria-label="Photo of a modern school building" style="height:210px;background:linear-gradient(180deg,#7fb6e0,#c9d4dc 55%,#6d7a52)"></div><p>Sed ut perspiciatis unde omnis</p><div class="bar"></div></div>
</section>

<footer class="abs footer">
  <p class="abs intro">If you need a guide for your child and want to know how we can help, kindly call us or fill out this form now.</p>
  <div class="abs field f1">Your Name</div>
  <div class="abs field f2">Phone No</div>
  <div class="abs field f3">Message</div>
  <div class="abs btn-green">SUBMIT</div>
  <div class="abs contact-card">
    <div class="txt"><b>Royal Athenaeum of Velmont</b><br>Rue des Tilleuls 12<br>4580 Velmont, Belgium</div>
    <div class="map" role="img" aria-label="Map showing the school location"></div>
  </div>
</footer>
<div class="abs copy">Copyright © Royal Athenaeum of Velmont 2019</div>

</body>
</html>
```